Flyers needed for new business Tidebloom

We have a colour and business & loyalty card currently on file, we would Ike similar colours and styles, flyers I think we make 3 folding,

Target Market(s)

We specialise in Magnesium float, infared saunas and hyperbaric oxygen chamber, all this is targeted for clients trying to manage chronic pain, weigh loss and detoxification

Industry/Entity Type

Health And Wellness

Font styles to use
Sans Serif
Decorative

Colors
33a6d7
85cae6
ffffff
9d9d9d

Requirements
Must have
• Business name an logo on front, middle I think we outline facilities and business outline, we are here to help our clients become their best selves through using our facilities we can assist them in the own journeys to becoming better able to manage chronic pain, weight loss that seems impossible to lose and provide the best meditative float experience they ever experienced
Nice to have
• Some photos of magnesium float tank, infrared sauna & oxygen chamber

```html
<!DOCTYPE html>
<html lang="en">
<head>
<meta charset="utf-8">
<title>Tidebloom Trifold Brochure</title>
<link rel="stylesheet" href="https://fonts.googleapis.com/css2?family=Raleway:wght@400;500;600;700;800&display=swap">
<style>
  :root{
    --blue:#07a3e6;
    --blue-deep:#0a86c7;
    --blue-soft:#85cae6;
    --blue-pale:#d3ecf8;
    --ink:#222222;
    --grey:#9d9d9d;
    --paper:#ffffff;
    --stage:#e6f3f8;
  }
  html,body{margin:0;padding:0;overflow:hidden}
  body{width:1200px;height:1200px;background:var(--stage);display:flex;align-items:center;justify-content:center}
  .brochure{width:1140px;height:880px;display:block;font-family:'Raleway',sans-serif}
  .heading{font-weight:700;fill:var(--ink)}
  .accent{fill:var(--blue)}
  .service-title{font-weight:700;font-size:20px;fill:var(--blue)}
  .service-text{font-size:15px;fill:var(--ink);font-weight:500}
  .lead{font-size:24px;fill:var(--ink);font-weight:400}
  .contact{font-size:16px;font-weight:700;fill:var(--ink);text-anchor:middle}
  .badge-text{font-weight:700;fill:var(--paper);text-anchor:middle}
  .hero-title{font-weight:800;font-size:60px;fill:var(--ink)}
</style>
</head>
<body>
<svg class="brochure" viewBox="76 205 1349 1041" xmlns="http://www.w3.org/2000/svg">
  <defs>
    <clipPath id="sheet"><rect x="76" y="205" width="1349" height="1041"/></clipPath>
    <clipPath id="left-panel"><rect x="76" y="205" width="450" height="1041"/></clipPath>
    <clipPath id="right-panel"><rect x="976" y="205" width="449" height="1041"/></clipPath>
    <linearGradient id="float-tone" x1="0" y1="0" x2="1" y2="1">
      <stop offset="0" stop-color="#5fc3e8"/>
      <stop offset="0.5" stop-color="#8fb9c4"/>
      <stop offset="1" stop-color="#2f9fd0"/>
    </linearGradient>
    <radialGradient id="sauna-tone" cx="0.45" cy="0.6" r="0.7">
      <stop offset="0" stop-color="#ff3a2a"/>
      <stop offset="0.7" stop-color="#d8141c"/>
      <stop offset="1" stop-color="#5a1410"/>
    </radialGradient>
    <radialGradient id="chamber-tone" cx="0.45" cy="0.45" r="0.6">
      <stop offset="0" stop-color="#f2f2f2"/>
      <stop offset="0.7" stop-color="#d8d8dc"/>
      <stop offset="1" stop-color="#6a6f9a"/>
    </radialGradient>
  </defs>

  <g clip-path="url(#sheet)">
    <!-- sheet and folds -->
    <rect class="sheet" x="76" y="205" width="1349" height="1041" fill="var(--paper)"/>
    <rect class="fold-shade" x="526" y="205" width="64" height="1041" fill="#f5f5f5"/>
    <rect class="fold-shade" x="935" y="205" width="41" height="1041" fill="#f5f5f5"/>

    <!-- sweeping arcs -->
    <path class="arc-wide" d="M380 1246 C470 760 760 420 1200 205 L1270 205 C820 440 560 780 490 1246 Z" fill="var(--blue-pale)" opacity="0.7"/>
    <path class="arc-band" d="M500 1246 C570 860 800 520 1060 330 L1080 350 C830 560 620 880 560 1246 Z" fill="var(--blue-soft)" opacity="0.55"/>

    <!-- left panel: bottom photo area -->
    <g clip-path="url(#left-panel)">
      <circle cx="200" cy="1320" r="490" fill="var(--blue-deep)"/>
      <circle cx="190" cy="1330" r="470" fill="var(--blue-soft)"/>
      <circle cx="180" cy="1340" r="455" fill="var(--blue)"/>
      <circle cx="170" cy="1350" r="440" fill="url(#sauna-tone)" role="img" aria-label="Photo of an infrared sauna cabin glowing red"/>
    </g>
    <circle cx="360" cy="968" r="114" fill="var(--blue-deep)"/>
    <circle cx="360" cy="960" r="112" fill="var(--blue)"/>
    <text class="badge-text" x="360" y="955" font-size="32">INFRARED</text>
    <text class="badge-text" x="360" y="988" font-size="32">SAUNAS</text>

    <!-- left panel copy -->
    <text class="heading" x="123" y="288" font-size="37">Experience</text>
    <text class="heading" x="123" y="335" font-size="37"><tspan class="accent">Nothingness</tspan>!</text>
    <rect x="123" y="357" width="85" height="2" fill="var(--blue)"/>
    <text class="lead" x="123" y="400">Lorem ipsum dolor sit amet,</text>
    <text class="lead" x="123" y="429">consectetur adipiscing elit</text>

    <text class="service-title" x="123" y="490">Magnesium float</text>
    <text class="service-text" x="123" y="513">In fringilla mauris dui, eget ornare</text>
    <text class="service-text" x="123" y="531">urna luctus vitae. Nullam a erat urna.</text>

    <text class="service-title" x="123" y="604">Infared saunas</text>
    <text class="service-text" x="123" y="627">In fringilla mauris dui, eget ornare</text>
    <text class="service-text" x="123" y="645">urna luctus vitae. Nullam a erat urna.</text>

    <text class="service-title" x="123" y="718">Hyperbaric oxygen</text>
    <text class="service-title" x="123" y="742">chamber</text>
    <text class="service-text" x="123" y="765">In fringilla mauris dui, eget ornare</text>
    <text class="service-text" x="123" y="783">urna luctus vitae. Nullam a erat urna.</text>

    <!-- middle panel -->
    <circle cx="755" cy="535" r="190" fill="var(--blue-deep)"/>
    <circle cx="758" cy="540" r="183" fill="var(--blue)"/>
    <circle cx="750" cy="525" r="175" fill="url(#chamber-tone)" role="img" aria-label="Photo of a white hyperbaric oxygen chamber with its door open"/>

    <g class="icon-pin" fill="var(--blue)">
      <path d="M751 794 a7 7 0 0 1 7 7 c0 6 -7 13 -7 13 c0 0 -7 -7 -7 -13 a7 7 0 0 1 7 -7z"/>
      <circle cx="751" cy="801" r="2.6" fill="var(--paper)"/>
    </g>
    <text class="contact" x="750" y="845">Your Address in</text>
    <text class="contact" x="750" y="866">Australia</text>

    <path class="icon-phone" d="M742 921 l5 -2 l3 6 l-3 3 c1.5 3 4 5.5 7 7 l3 -3 l6 3 l-2 5 c-10 0 -19 -9 -19 -19z" fill="var(--blue)"/>
    <text class="contact" x="750" y="968">Your Phone goes here</text>
    <text class="contact" x="750" y="988" font-size="14">+ 1111-1111-222222</text>

    <g class="icon-mail">
      <rect x="738" y="1068" width="25" height="18" rx="2" fill="var(--blue)"/>
      <path d="M739 1070 l11.5 9 l11.5 -9" fill="none" stroke="var(--paper)" stroke-width="2"/>
    </g>
    <text class="contact" x="750" y="1127">youremail@mail.com</text>

    <rect x="582" y="1178" width="337" height="110" rx="55" fill="var(--blue)"/>
    <text class="badge-text" x="750" y="1220" font-size="17">www.yourwebsite.com</text>

    <!-- right panel -->
    <g clip-path="url(#right-panel)">
      <path d="M1180 205 L1425 205 L1425 955 C1230 950 1060 820 1028 640 C1010 520 1050 360 1180 205 Z" fill="var(--blue-deep)"/>
      <circle cx="1340" cy="560" r="330" fill="var(--blue)"/>
      <circle cx="1345" cy="555" r="315" fill="url(#float-tone)" role="img" aria-label="Photo of a woman floating peacefully in blue water"/>
    </g>
    <circle cx="1143" cy="372" r="139" fill="var(--blue-deep)"/>
    <circle cx="1141" cy="367" r="136" fill="var(--blue)"/>
    <text class="badge-text" x="1141" y="384" font-size="44">Tidebloom</text>

    <text class="hero-title" x="1022" y="922">Float</text>
    <text class="hero-title accent" x="1022" y="983">To be</text>
    <text class="hero-title" x="1022" y="1045">Healther!</text>
    <rect x="1022" y="1075" width="75" height="2" fill="var(--blue)"/>
    <text class="lead" x="1022" y="1128">Use of the best ultra silent float</text>
    <text class="lead" x="1022" y="1157">with a new therapeutic</text>
    <text class="lead" x="1022" y="1186">treatment growing in popularity</text>
  </g>
</svg>
</body>
</html>
```